Business Card for Corinne Waldo

Name: Corinne Waldo
Title: Realtor
Email: Corinne@CorinneWaldoRE.example
Phone: 555-318-7492

On the front of the business card, I would like the photo, the contact information and the Corinne Waldo Logo. The backside is required to have the Broker logo and the required logos. Please use the colors from the logo design. Our company has a classy, professional look.

```html
<!DOCTYPE html>
<html lang="en">
<head>
<meta charset="utf-8">
<title>Corinne Waldo – Business Card</title>
<link rel="stylesheet" href="https://fonts.googleapis.com/css2?family=Cinzel:wght@400;600&family=Tinos:ital@0;1&display=swap">
<style>
  :root {
    --backdrop: #6b6768;
    --card-black: #141414;
    --card-charcoal: #2c2c2c;
    --card-white: #f7f7f7;
    --brand-red: #a52232;
    --ink: #3a3a3a;
    --white: #ffffff;
  }
  * { box-sizing: border-box; margin: 0; padding: 0; }
  html, body { width: 1200px; height: 1200px; overflow: hidden; }
  body { background: var(--backdrop); position: relative; font-family: "Tinos", "Times New Roman", serif; }

  .card {
    position: absolute; top: 296px; width: 348px; height: 592px;
    border-radius: 22px; overflow: hidden;
  }

  /* Back side */
  .card-back { left: 200px; background: var(--card-black); }
  .back-pattern {
    position: absolute; inset: 0;
    background: radial-gradient(ellipse at 50% 25%, var(--card-charcoal) 0%, var(--card-black) 70%);
  }
  .broker-mark {
    position: absolute; left: 50%; top: 150px; width: 96px; height: 96px;
    transform: translateX(-50%); border: 2px solid var(--white); border-radius: 50%;
  }
  .broker-name {
    position: absolute; left: 0; right: 0; top: 300px; text-align: center;
    color: var(--white); font-family: "Cinzel", serif; font-weight: 600;
    font-size: 18px; letter-spacing: 3px; line-height: 1;
  }
  .broker-sub {
    position: absolute; left: 0; right: 0; top: 326px; text-align: center;
    color: var(--white); font-family: "Cinzel", serif; font-weight: 600;
    font-size: 10px; letter-spacing: 2px;
  }
  .badges { position: absolute; top: 489px; left: 115px; display: flex; gap: 6px; align-items: flex-end; }
  .badge { background: var(--white); }
  .badge-housing { width: 40px; height: 34px; }
  .badge-member { width: 26px; height: 34px; }
  .badge-listing { width: 60px; height: 30px; }
  .back-web {
    position: absolute; left: 0; right: 0; top: 550px; text-align: center;
    color: var(--white); font-size: 15px;
  }

  /* Front side */
  .card-front { left: 637px; background: var(--card-white); }
  .side-band { position: absolute; left: 0; top: 0; bottom: 0; width: 74px; background: var(--brand-red); }
  .brand-name {
    position: absolute; left: 92px; top: 58px; color: var(--brand-red);
    font-family: "Cinzel", serif; font-weight: 400; font-size: 24px; letter-spacing: 0.3px; line-height: 1;
    white-space: nowrap;
  }
  .brand-sub {
    position: absolute; right: 34px; top: 90px; color: var(--brand-red);
    font-family: "Cinzel", serif; font-weight: 400; font-size: 11px; letter-spacing: 1px;
  }
  .agent-name {
    position: absolute; left: 92px; top: 132px; color: var(--ink);
    font-family: "Cinzel", serif; font-size: 24px; letter-spacing: 0.3px; line-height: 1;
    white-space: nowrap;
  }
  .agent-title {
    position: absolute; left: 93px; top: 164px; color: var(--brand-red);
    font-style: italic; font-size: 16px;
  }
  .contact-list { position: absolute; left: 94px; right: 14px; top: 214px; list-style: none; }
  .contact-item { display: flex; align-items: center; height: 23px; color: var(--ink); font-size: 14.5px; white-space: nowrap; }
  .contact-icon { width: 12px; height: 12px; margin-right: 12px; flex: none; }
  .agent-photo {
    position: absolute; left: 128px; top: 334px; right: 0; bottom: 0;
    background: radial-gradient(ellipse at 55% 45%, #d8d8d8 0%, #a9a9a9 45%, #3b3b3b 100%);
  }
</style>
</head>
<body>
  <section class="card card-back" aria-label="Card back">
    <div class="back-pattern" role="img" aria-label="Faint tonal monogram pattern across the card"></div>
    <div class="broker-mark"></div>
    <div class="broker-name">HARLAN PRYCE</div>
    <div class="broker-sub">REAL ESTATE</div>
    <div class="badges" aria-label="Required compliance badges">
      <span class="badge badge-housing"></span>
      <span class="badge badge-member"></span>
      <span class="badge badge-listing"></span>
    </div>
    <div class="back-web">www.CorinneWaldoRE.example</div>
  </section>

  <section class="card card-front" aria-label="Card front">
    <div class="side-band"></div>
    <div class="brand-name">CORINNE WALDO</div>
    <div class="brand-sub">REAL ESTATE</div>
    <div class="agent-name">CORINNE WALDO</div>
    <div class="agent-title">Realtor/Broker</div>
    <ul class="contact-list">
      <li class="contact-item">
        <svg class="contact-icon" viewBox="0 0 12 12" aria-hidden="true"><path fill="#a52232" d="M1 3c0-1 1-2 5-2s5 1 5 2v1H8V3H4v1H1zM3 5h6l2 3v3H1V8z"/></svg>
        555-318-7492
      </li>
      <li class="contact-item">
        <svg class="contact-icon" viewBox="0 0 12 12" aria-hidden="true"><rect x="0.5" y="2" width="11" height="8" fill="#a52232"/><path d="M0.5 2l5.5 4.5L11.5 2" fill="none" stroke="#f7f7f7" stroke-width="1"/></svg>
        Corinne@CorinneWaldoRE.example
      </li>
      <li class="contact-item">
        <svg class="contact-icon" viewBox="0 0 12 12" aria-hidden="true"><circle cx="6" cy="6" r="5.5" fill="#a52232"/><path d="M0.5 6h11M6 0.5v11M2 3.2h8M2 8.8h8" stroke="#f7f7f7" stroke-width="0.7" fill="none"/><ellipse cx="6" cy="6" rx="2.5" ry="5.5" fill="none" stroke="#f7f7f7" stroke-width="0.7"/></svg>
        www.CorinneWaldoRE.example
      </li>
    </ul>
    <div class="agent-photo" role="img" aria-label="Black and white portrait photo of Corinne Waldo"></div>
  </section>
</body>
</html>
```